Flyer Design For Building & Decorating Company

We need an A6 double-sided colour flyer for a letter-box marketing campaign. We are a building and decorating company based in West London. We saw a flyer that we liked and have attached it as an example of the sort of thing we're looking for (see attached files Example A6 Flyer - Front.png and Example A6 Flyer - Back.png). Please note that we're not expecting the designer to slavishly follow this design, more to use it as a jumping-off point.

The design must incorporate a strong call to action, e.g., Call Us For A Free, No-Obligation Quote.

The textual information that must be included in the flyer (contact methods, tagline, services, etc.) are included in the attached file Flyer Text.docx.

Also included as attachments are a selection of images used on our website (files bathroom.png, carpentry.png, decorating.jpg,
flooring.jpg, painting_decorating.jpg, repointing.jpg and work_ on_scaffold.jpg). Please include these images on the flyer (at least one image on each side), or use stock images if any of these are unsuitable.

The company logo will also need to be included in the flyer - see attached file logo.png

The images on our website have all had to be re-sized from the originals. I've attached a number of the original images to this brief, as these are the highest resolution versions of the images that we have. I would ask that you use the versions attached to the brief, but if you feel that other images from our website would work better on your flyer design, please let me know and I'll attach them to this brief.

Finally, we've attached guideline notes from our printer (see attached file Printer's Requirements.docx) - please ensure these are adhered to where relevant.

Target Market(s)

People in West London who require building or decorating work to be done on their properties.

Industry/Entity Type

Marketing

Requirements
Must have
• A6 double-sided colour flyer using the text we provided and some of the images provided.

The call to action must be prominent and eye-catching, as the only purpose of the flyer is to get recipients to contact our company for a quote.

```html
<!DOCTYPE html>
<html lang="en">
<head>
<meta charset="utf-8">
<title>K &amp; M Renovations – A6 Flyer</title>
<link href="https://fonts.googleapis.com/css2?family=Lato:ital,wght@0,400;0,700;0,900;1,900&display=swap" rel="stylesheet">
<style>
  :root {
    --orange: #ff3300;
    --orange-soft: #ff6a47;
    --cream: #eefbc6;
    --red-text: #ea2a0c;
    --white: #ffffff;
    --ink-soft: #ffe9e0;
  }
  * { box-sizing: border-box; margin: 0; padding: 0; }
  html, body { width: 1200px; height: 1000px; overflow: hidden; background: var(--white); }
  body { position: relative; font-family: "Lato", Arial, sans-serif; color: var(--white); }

  .panel { position: absolute; top: 125px; width: 518px; height: 723px; background: var(--orange); overflow: hidden; }
  .front { left: 66px; }
  .back { left: 618px; }

  /* Front */
  .brand { position: absolute; left: 34px; top: 34px; width: 130px; height: 120px;
    display: flex; flex-direction: column; align-items: center; justify-content: center; gap: 8px; }
  .brand-mark { width: 22px; height: 22px; background: var(--cream); }
  .brand-name { font-weight: 700; font-size: 17px; line-height: 1.15; text-align: center; color: var(--cream); letter-spacing: .5px; }
  .tagline { position: absolute; left: 170px; top: 50px; width: 320px; text-align: center;
    font-weight: 900; font-style: italic; font-size: 19px; line-height: 24px; letter-spacing: 1px; }
  .contact-strip { position: absolute; left: 0; top: 172px; width: 100%; height: 50px; background: var(--orange-soft);
    text-align: center; font-size: 13px; line-height: 19px; padding-top: 6px; letter-spacing: .2px; }
  .contact-strip span + span { margin-left: 18px; }
  .photo { position: absolute; border: 3px solid var(--white); }
  .photo-kitchen { left: 38px; top: 240px; width: 207px; height: 140px; background: linear-gradient(135deg, #8a7a55, #c9c3a6 55%, #5b4a32); }
  .photo-flooring { left: 271px; top: 240px; width: 205px; height: 140px; background: linear-gradient(135deg, #e8e4de, #c99a5e 55%, #a36d32); }
  .service-list { position: absolute; left: 0; top: 400px; width: 100%; text-align: center;
    font-weight: 700; font-size: 15.5px; line-height: 25px; letter-spacing: .6px; }
  .cta { position: absolute; left: 0; top: 495px; width: 100%; height: 228px; background: var(--cream); color: var(--red-text); }
  .cta-head { position: absolute; left: 29px; top: 22px; font-weight: 900; font-size: 26px; line-height: 32px; letter-spacing: .2px; }
  .cta-tick { position: absolute; left: 430px; top: 16px; }
  .cta-phone-icon { position: absolute; left: 26px; top: 102px; }
  .cta-numbers { position: absolute; left: 118px; top: 92px; font-weight: 900; font-size: 51px; line-height: 56px; letter-spacing: 2px; }

  /* Back */
  .back-header { position: absolute; left: 0; top: 0; width: 100%; height: 47px; background: var(--cream); color: var(--orange);
    display: flex; align-items: center; padding-left: 17px; gap: 6px; font-weight: 900; font-size: 16.5px; letter-spacing: .3px; }
  .service-block { position: absolute; left: 0; width: 480px; height: 142px; background: var(--orange-soft); }
  .service-block h2 { position: absolute; left: 29px; top: 12px; font-weight: 900; font-size: 15.5px; letter-spacing: 1.2px; }
  .service-block ul { position: absolute; left: 29px; top: 32px; list-style: none; font-size: 14.5px; line-height: 20.3px; }
  .service-block .shot { position: absolute; right: 0; top: 0; width: 208px; height: 142px; }
  .block-bathroom { top: 60px; }
  .block-carpentry { top: 229px; }
  .block-repairs { top: 398px; }
  .block-repairs h2 { top: 18px; }
  .block-repairs ul { top: 38px; }
  .block-decorating { top: 567px; width: 344px; height: 143px; }
  .block-decorating h2 { top: 10px; }
  .block-decorating ul { top: 29px; font-size: 13px; line-height: 18.2px; }
  .block-decorating .shot { width: 142px; height: 143px; }
  .shot-bathroom { background: linear-gradient(120deg, #f1f1ef, #2f5d9a 50%, #c5c9cc); }
  .shot-carpentry { background: linear-gradient(135deg, #c99a6a, #ead4b6 55%, #a5763f); }
  .shot-repairs { background: linear-gradient(180deg, #8aa07a, #3b3d40 40%, #2c2e31); }
  .shot-decorating { background: linear-gradient(135deg, #d8d4cb, #f2efe8 50%, #c7a48e); }
  .more { position: absolute; left: 362px; top: 585px; font-weight: 900; line-height: 1; }
  .more .small { font-size: 22px; letter-spacing: .5px; }
  .more .big { font-size: 32px; line-height: 40px; letter-spacing: 1px; }
</style>
</head>
<body>

<section class="panel front">
  <div class="brand">
    <div class="brand-mark"></div>
    <div class="brand-name">K &amp; M<br>RENOVATIONS</div>
  </div>
  <p class="tagline">‘WEST LONDON BUILDERS &amp; DECORATORS<br>QUALITY RENOVATIONS AT AFFORDABLE PRICES’</p>
  <div class="contact-strip">
    <div>K &amp; M Renovations, 14 Larch Grove, Ealing, London W5 3QT</div>
    <div><span>Email: hello@km-renovations.co.uk</span><span>Web: www.km-renovations.co.uk</span></div>
  </div>
  <div class="photo photo-kitchen" role="img" aria-label="Photo of a renovated fitted kitchen with cream units and a large window"></div>
  <div class="photo photo-flooring" role="img" aria-label="Photo of hands marking a roll of wood-effect vinyl flooring with a tape measure"></div>
  <div class="service-list">
    <div>Bathroom/Kitchens &nbsp;•&nbsp; Tiling &nbsp;•&nbsp; Painting/Decorating</div>
    <div>Plastering &nbsp;•&nbsp; Carpentry &nbsp;•&nbsp; Flooring &nbsp;•&nbsp; Plumbing</div>
    <div>Electrical Works &nbsp;•&nbsp; Brickwork &nbsp;•&nbsp; General Repairs</div>
  </div>
  <div class="cta">
    <p class="cta-head">CALL US NOW FOR A FREE<br>NO-OBLIGATION QUOTE</p>
    <svg class="cta-tick" width="62" height="62" viewBox="0 0 62 62" aria-hidden="true">
      <circle cx="28" cy="34" r="24" fill="none" stroke="var(--red-text)" stroke-width="4"/>
      <path d="M15 33 L26 45 L56 6" fill="none" stroke="var(--red-text)" stroke-width="6" stroke-linecap="round" stroke-linejoin="round"/>
    </svg>
    <svg class="cta-phone-icon" width="80" height="80" viewBox="0 0 80 80" aria-hidden="true">
      <circle cx="40" cy="40" r="36" fill="none" stroke="var(--red-text)" stroke-width="4"/>
      <path d="M26 20 c-6 4 -8 10 -4 20 c5 11 12 18 22 22 c8 3 13 1 16 -4 l-9 -8 c-2 2 -5 3 -8 1 c-5 -3 -9 -8 -11 -12 c-1 -3 0 -5 2 -7 z" fill="none" stroke="var(--red-text)" stroke-width="4" stroke-linejoin="round"/>
    </svg>
    <p class="cta-numbers">0208 555 0142<br>07700 900461</p>
  </div>
</section>

<section class="panel back">
  <header class="back-header">
    <span>K &amp; M RENOVATIONS</span>
    <svg width="20" height="20" viewBox="0 0 20 20" aria-hidden="true">
      <circle cx="10" cy="10" r="8.5" fill="none" stroke="var(--orange)" stroke-width="2"/>
      <path d="M7 5 c-2 1 -2 3 -1 5 c1 2 3 4 5 5 c2 1 3 0 4 -1 l-2 -2 c-1 1 -2 1 -3 0 c-1 -1 -2 -2 -2 -3 c0 -1 0 -1 1 -2 z" fill="var(--orange)"/>
    </svg>
    <span>0208 5550142 • 07700 900461</span>
  </header>

  <article class="service-block block-bathroom">
    <h2>BATHROOM/KITCHEN</h2>
    <ul>
      <li>- Complete/Partial Fixings</li>
      <li>- Tiling</li>
      <li>- Sink/Bath/Radiator</li>
      <li>- Tap Repairs/Replace</li>
      <li>- Fit Washing Machine/Dishwasher</li>
    </ul>
    <div class="shot shot-bathroom" role="img" aria-label="Photo of a finished bathroom with blue panelling, radiator and toilet"></div>
  </article>

  <article class="service-block block-carpentry">
    <h2>CARPENTRY</h2>
    <ul>
      <li>- Wardrobes/Cupboards</li>
      <li>- Shelving/Skirting</li>
      <li>- Doors/Windows</li>
      <li>- Kitchen/Bathroom Suites</li>
      <li>- Wooden Floor/Laminate</li>
    </ul>
    <div class="shot shot-carpentry" role="img" aria-label="Photo of a carpenter marking timber with a pencil and square beside a hammer"></div>
  </article>

  <article class="service-block block-repairs">
    <h2>MAINTENANCE/REPAIRS</h2>
    <ul>
      <li>- Reseal Bath/Shower</li>
      <li>- Fit Shelves</li>
      <li>- Electrics - Complete/Partial</li>
      <li>- Sash/Gutter/Roof Repairs</li>
    </ul>
    <div class="shot shot-repairs" role="img" aria-label="Photo of roofers laying felt on a flat roof with a gas torch"></div>
  </article>

  <article class="service-block block-decorating">
    <h2>DECORATING</h2>
    <ul>
      <li>- Complete/Partial Works</li>
      <li>- Lining/Wallpaper</li>
      <li>- Painting Inside/Outside</li>
      <li>- Plastering/Skimming</li>
      <li>- Rectify Damage</li>
      <li>- Freshen Paintwork</li>
    </ul>
    <div class="shot shot-decorating" role="img" aria-label="Photo of hands fitting white coving to a ceiling"></div>
  </article>

  <div class="more">
    <div class="small">AND</div>
    <div class="big">LOTS<br>MORE...</div>
  </div>
</section>

</body>
</html>
```